job report

Designer – Professional Plumbing Job Report Template

Overview

We are seeking a skilled designer to create a professional, easy-to-use Job Report template for a commercial and maintenance plumbing business.
The report will be used for clients, property managers, facilities managers, strata, and retail centres and must clearly communicate findings, works completed, and recommendations in a polished, compliant, and branded format.

The final document must be suitable for PDF delivery, email, and ongoing reuse.

Objectives

Present plumbing works in a clear, professional, and defensible report format

Improve client understanding of findings and recommendations

Provide a repeatable template that can be used across maintenance, reactive, and investigative works

Allow easy insertion of text, tables, and photos

Report Structure (Minimum Inclusions)
1. Cover Page

Company logo and branding

Report title (e.g. Plumbing Job Report / Investigation Report)

Client name

Site address

Job reference / work order number

Date of attendance

Technician / contractor name

2. Client & Site Details

Client / company name

Site address

Contact person

Contact details

Access notes (after-hours, tenant access, etc.)

3. Reason for Attendance

Clear description of why attendance was required

Call-out type (reactive, scheduled maintenance, investigation, emergency, etc.)

Reported issue or scope requested by client

4. Findings / Observations

Detailed findings discovered on site

Condition of pipework, fixtures, drainage, or systems

Any contributing factors identified

Notes on compliance, wear, damage, or risk

(This section should support bullet points and paragraphs.)

5. Works Carried Out

Step-by-step description of works completed

Equipment used (e.g. jetter, CCTV camera, leak detection, flex shaft, etc.)

Repairs, replacements, testing, and verification

Confirmation that systems were tested and operational on completion

6. Photos & Visual Evidence

Clearly labelled photo sections

Before / during / after photos

Space for photo captions and explanations

Logical layout that aligns photos with written findings

7. Recommendations

Clearly separated from works completed

Urgent vs non-urgent recommendations

Preventative maintenance advice

Upgrade or replacement suggestions

Risk-based language where appropriate

8. Limitations & Exclusions

Areas not inspected

Access limitations

Assumptions made during inspection

Items outside scope of works

9. Conclusion

Summary of outcome

Confirmation of current system status

Next steps (if any)

10. Sign-Off

Contractor / technician name

Company name

Date

Optional client acknowledgement section

Design Requirements

Clean, professional layout

Commercial / trade-appropriate styling (not overly creative)

Easy-to-read fonts

Consistent headings and spacing

Logical flow for busy property managers

Editable format (Word / Google Docs / InDesign source file)

Final export-ready PDF version

Bonus (Nice to Have)

Traffic-light system (Green / Amber / Red) for condition reporting

Iconography for findings, repairs, and recommendations

Optional sections for compliance notes (AS/NCC references)

Space for QR codes or job reference numbers

Deliverables

Editable master report template

PDF version

Instructions or notes for ongoing use

```html
<!DOCTYPE html>
<html lang="en">
<head>
<meta charset="utf-8">
<title>Plumbing Job Report – Template Pages</title>
<link href="https://fonts.googleapis.com/css2?family=Barlow+Semi+Condensed:wght@500;600;700&family=Arimo:wght@400;700&display=swap" rel="stylesheet">
<style>
:root{
  --board:#474747;
  --navy:#1b3a5e;
  --sky:#29b6e0;
  --sky-soft:#cdeef9;
  --sun:#f5c13e;
  --olive:#b5a843;
  --ink:#1a1a1a;
  --muted:#666;
  --rule:#555;
  --red:#e3202a;
  --amber:#f39a1f;
  --green:#2fa84f;
  --head:"Barlow Semi Condensed",sans-serif;
  --body:"Arimo",sans-serif;
}
*{margin:0;padding:0;box-sizing:border-box}
html,body{width:1200px;height:852px;overflow:hidden;background:var(--board)}
.board{position:relative;width:1200px;height:852px}
.page{position:absolute;width:227px;height:322px;overflow:hidden;font-family:var(--body);color:var(--ink);
  background:linear-gradient(180deg,#fff 0%,#fff 72%,var(--sky-soft) 100%);box-shadow:2px 3px 6px rgba(0,0,0,.45)}
.page > *{position:absolute}
.header-swoosh{top:0;left:0;width:227px;height:40px}
.brand{left:14px;top:17px;display:flex;align-items:center;gap:3px;font-family:var(--head);font-weight:700;color:var(--sky);font-size:10px;line-height:.95;letter-spacing:.2px}
.brand-dot{width:7px;height:7px;border-radius:50%;background:var(--sun);flex:none}
.section-title{left:0;width:100%;text-align:center;font-family:var(--head);font-weight:700;font-size:13px;color:var(--sky);letter-spacing:.3px;line-height:1}
.field{display:flex;align-items:flex-end;gap:2px;font-size:4.4px;height:6px}
.field .rule{flex:1;border-bottom:.5px solid var(--rule);height:4px}
.write-line{height:0;border-bottom:.5px solid var(--rule)}
.label-bold{font-weight:700;font-size:6px}
.note{font-size:4.4px}
.note em{font-style:normal;color:var(--muted)}
.bullet{display:flex;align-items:center;gap:4px;font-size:4.4px}
.drop{width:6px;height:6px;border-radius:50%;background:radial-gradient(circle at 50% 60%,#fff 0 28%,var(--navy) 32%);flex:none}
.check{display:flex;align-items:center;gap:3px;font-size:5px}
.check i{width:5px;height:5px;border:.5px solid #444;display:block}
.check.sm{font-size:4.4px}
.check.sm i{width:4.5px;height:4.5px}
.footer-band{left:0;bottom:0;width:227px;height:17px;background:var(--sky)}
.footer-band.light{left:181px;width:46px;background:var(--sky-soft);border-radius:9px 0 0 0}
.footer-url{left:0;top:297px;width:94px;height:13px;border-radius:0 7px 7px 0;background:var(--sun);
  font-family:var(--head);font-weight:600;font-size:6px;display:flex;align-items:center;justify-content:center;color:var(--ink)}
.footer-page{left:162px;top:297px;width:65px;height:13px;border-radius:7px 0 0 7px;background:var(--olive);
  font-family:var(--head);font-size:5px;display:flex;align-items:center;justify-content:center;padding-left:8px;color:#222}

/* cover */
.cover{background:#000}
.cover .brand{left:19px;top:20px;font-size:14px}
.cover .brand-dot{width:9px;height:9px}
.cover-kicker{left:0;width:100%;top:60px;text-align:center;font-family:var(--head);font-weight:600;font-size:18px;color:#fff;letter-spacing:.5px}
.cover-title{left:0;width:100%;top:76px;text-align:center;font-family:var(--head);font-weight:700;font-size:54px;color:var(--sun);line-height:1;letter-spacing:1px}
.cover-art{left:0;top:120px;width:227px;height:202px}
.cover-form{left:26px;top:221px;display:grid;grid-template-columns:65px 107px;column-gap:3px;row-gap:3.5px}
.cover-form span{background:var(--sun);font-size:4.8px;height:7.3px;line-height:7.3px;padding-left:4px}
.cover-form b{background:#fff;height:7.3px;display:block}
.cover .footer-url{left:133px;width:94px;border-radius:7px 0 0 7px}
.cover-bluepill{left:44px;top:305px;width:183px;height:17px;background:var(--sky);border-radius:9px 0 0 9px}

/* photos */
.photo-card{border:1.5px solid var(--sky);border-radius:4px;background:#fff}
.photo-card h4{text-align:center;font-family:var(--head);font-weight:600;font-size:6.5px;color:var(--sky);margin-top:3px}
.photo-fill{position:absolute;left:3px;right:3px;top:13px;height:57px}
.photo-card .write-line{position:absolute;left:3px;right:3px}

/* recommendations */
.priority{display:flex;gap:6px;align-items:flex-start}
.priority .badge{width:15px;height:15px;border-radius:50%;display:flex;align-items:center;justify-content:center;flex:none}
.priority .badge::after{content:"";width:8px;height:2px;background:#fff;border-radius:1px}
.priority strong{display:block;font-size:6px;margin-top:1px}
.priority small{display:block;font-size:4.2px;color:var(--muted);margin-top:2px}
</style>
</head>
<body>
<main class="board">

  <!-- Cover -->
  <section class="page cover" style="left:107px;top:91px">
    <div class="brand"><span class="brand-dot"></span><span>HARBOURLINE<br>PLUMBING</span></div>
    <div class="cover-kicker">PLUMBING JOB</div>
    <div class="cover-title">REPORT</div>
    <svg class="cover-art" viewBox="0 0 227 202" aria-hidden="false">
      <defs>
        <linearGradient id="roomTone" x1="0" y1="0" x2="0.3" y2="1">
          <stop offset="0" stop-color="#1d3b66"/><stop offset=".6" stop-color="#2a4f78"/><stop offset="1" stop-color="#c9863c"/>
        </linearGradient>
        <radialGradient id="pitTone" cx=".5" cy=".5" r=".6">
          <stop offset="0" stop-color="#8a7a66"/><stop offset="1" stop-color="#3f3024"/>
        </radialGradient>
      </defs>
      <path d="M0 80 C40 40 80 60 120 70 C170 80 200 60 227 75 V202 H0 Z" fill="url(#roomTone)" role="img" aria-label="Photo of a plumbing tank installation indoors"/>
      <path d="M0 80 C40 40 80 60 120 70 C170 80 200 60 227 75 V82 C200 70 170 88 120 78 C80 68 40 52 0 96 Z" fill="var(--sky)"/>
      <circle cx="164" cy="51" r="42" fill="var(--sun)"/>
      <circle cx="164" cy="51" r="39" fill="var(--sky)"/>
      <circle cx="164" cy="51" r="36" fill="url(#pitTone)" role="img" aria-label="Photo of exposed pipework in an excavated trench"/>
    </svg>
    <div class="cover-form">
      <span>Company Name:</span><b></b>
      <span>Client Name:</span><b></b>
      <span>Site Address:</span><b></b>
      <span>Job / Work Order No.:</span><b></b>
      <span>Date of Attendance:</span><b></b>
      <span>Technician / Contractor:</span><b></b>
    </div>
    <div class="cover-bluepill"></div>
    <div class="footer-url">harbourlineplumbing.com.au</div>
  </section>

  <!-- Page 1 -->
  <section class="page" style="left:360px;top:91px">
    <svg class="header-swoosh" viewBox="0 0 227 40"><path d="M67 0 C80 22 92 32 120 33 L227 29 V34 L120 37 C90 37 78 28 63 0 Z" fill="var(--sun)"/><path d="M67 0 C80 20 92 30 120 30 L227 27 V0 Z" fill="var(--navy)"/></svg>
    <div class="brand"><span class="brand-dot"></span><span>HARBOURLINE<br>PLUMBING</span></div>
    <h2 class="section-title" style="top:86px">CLIENT INFORMATION</h2>
    <div class="field" style="left:36px;top:109px;width:153px">Client / Company Name:<span class="rule"></span></div>
    <div class="field" style="left:36px;top:120px;width:153px">Contact Person:<span class="rule"></span></div>
    <div class="field" style="left:36px;top:131px;width:153px">Phone:<span class="rule"></span>Email:<span class="rule"></span></div>
    <h2 class="section-title" style="top:163px">SITE INFORMATION</h2>
    <div class="field" style="left:36px;top:185px;width:153px">Site Address:<span class="rule"></span></div>
    <div class="write-line" style="left:36px;top:205px;width:153px"></div>
    <div class="write-line" style="left:36px;top:220px;width:153px"></div>
    <p class="note" style="left:36px;top:230px">Access Notes: <em>(e.g. after-hours access, tenant coordination, restricted areas)</em></p>
    <div class="footer-band"></div>
    <div class="footer-url">harbourlineplumbing.com.au</div>
    <div class="footer-page">Page 1</div>
  </section>

  <!-- Page 2 -->
  <section class="page" style="left:613px;top:91px">
    <svg class="header-swoosh" viewBox="0 0 227 40"><path d="M67 0 C80 22 92 32 120 33 L227 29 V34 L120 37 C90 37 78 28 63 0 Z" fill="var(--sun)"/><path d="M67 0 C80 20 92 30 120 30 L227 27 V0 Z" fill="var(--navy)"/></svg>
    <div class="brand"><span class="brand-dot"></span><span>HARBOURLINE<br>PLUMBING</span></div>
    <h2 class="section-title" style="top:86px">REASON FOR ATTENDANCE</h2>
    <p class="label-bold" style="left:29px;top:114px">Call-Out Type:</p>
    <div class="check" style="left:29px;top:126px"><i></i>Reactive</div>
    <div class="check" style="left:123px;top:126px"><i></i>Investigation</div>
    <div class="check" style="left:29px;top:137px"><i></i>Scheduled Maintenance</div>
    <div class="check" style="left:123px;top:137px"><i></i>Emergency</div>
    <p class="label-bold" style="left:29px;top:167px">Reported Issue / Scope Requested:</p>
    <div class="write-line" style="left:29px;top:185px;width:160px"></div>
    <div class="write-line" style="left:29px;top:201px;width:160px"></div>
    <div class="write-line" style="left:29px;top:216px;width:160px"></div>
    <div class="write-line" style="left:29px;top:231px;width:160px"></div>
    <div class="footer-band"></div>
    <div class="footer-url">harbourlineplumbing.com.au</div>
    <div class="footer-page">Page 2</div>
  </section>

  <!-- Page 3 -->
  <section class="page" style="left:866px;top:91px">
    <svg class="header-swoosh" viewBox="0 0 227 40"><path d="M67 0 C80 22 92 32 120 33 L227 29 V34 L120 37 C90 37 78 28 63 0 Z" fill="var(--sun)"/><path d="M67 0 C80 20 92 30 120 30 L227 27 V0 Z" fill="var(--navy)"/></svg>
    <div class="brand"><span class="brand-dot"></span><span>HARBOURLINE<br>PLUMBING</span></div>
    <h2 class="section-title" style="top:86px">FINDINGS &amp; OBSERVATIONS</h2>
    <div class="bullet" style="left:28px;top:109px"><span class="drop"></span>Condition of pipework, fixtures, drainage, and related systems</div>
    <div class="bullet" style="left:28px;top:120px"><span class="drop"></span>Visible wear, damage, corrosion, or failure identified</div>
    <div class="bullet" style="left:28px;top:131px"><span class="drop"></span>Contributing factors observed (age, blockage, misuse, environmental conditions)</div>
    <div class="bullet" style="left:28px;top:142px"><span class="drop"></span>Compliance observations (where applicable)</div>
    <div class="bullet" style="left:28px;top:153px"><span class="drop"></span>Potential risks or future failure points</div>
    <p class="label-bold" style="left:29px;top:182px">Additional Notes:</p>
    <div class="write-line" style="left:29px;top:200px;width:160px"></div>
    <div class="write-line" style="left:29px;top:215px;width:160px"></div>
    <div class="write-line" style="left:29px;top:230px;width:160px"></div>
    <div class="write-line" style="left:29px;top:245px;width:160px"></div>
    <div class="footer-band"></div>
    <div class="footer-url">harbourlineplumbing.com.au</div>
    <div class="footer-page">Page 3</div>
  </section>

  <!-- Page 4 -->
  <section class="page" style="left:107px;top:439px">
    <svg class="header-swoosh" viewBox="0 0 227 40"><path d="M67 0 C80 22 92 32 120 33 L227 29 V34 L120 37 C90 37 78 28 63 0 Z" fill="var(--sun)"/><path d="M67 0 C80 20 92 30 120 30 L227 27 V0 Z" fill="var(--navy)"/></svg>
    <div class="brand"><span class="brand-dot"></span><span>HARBOURLINE<br>PLUMBING</span></div>
    <h2 class="section-title" style="top:87px">WORKS CARRIED OUT</h2>
    <div class="bullet" style="left:28px;top:109px"><span class="drop"></span>Isolated water / services as required</div>
    <div class="bullet" style="left:28px;top:120px"><span class="drop"></span>Completed repairs, replacements, or adjustments</div>
    <div class="bullet" style="left:28px;top:131px"><span class="drop"></span>Equipment used:</div>
    <div class="check sm" style="left:43px;top:144px"><i></i>High-pressure jetter</div>
    <div class="check sm" style="left:43px;top:151px"><i></i>CCTV inspection camera</div>
    <div class="check sm" style="left:43px;top:158px"><i></i>Leak detection equipment</div>
    <div class="check sm" style="left:43px;top:165px"><i></i>Flex shaft / mechanical tools</div>
    <div class="bullet" style="left:28px;top:178px"><span class="drop"></span>All works completed in accordance with industry standards</div>
    <div class="bullet" style="left:28px;top:191px"><span class="drop"></span>System tested and verified operational upon completion</div>
    <p class="label-bold" style="left:29px;top:213px">Work Completion Notes:</p>
    <div class="write-line" style="left:29px;top:231px;width:160px"></div>
    <div class="write-line" style="left:29px;top:247px;width:160px"></div>
    <div class="write-line" style="left:29px;top:262px;width:160px"></div>
    <div class="write-line" style="left:29px;top:278px;width:160px"></div>
    <div class="footer-band"></div>
    <div class="footer-url">harbourlineplumbing.com.au</div>
    <div class="footer-page">Page 4</div>
  </section>

  <!-- Page 5 -->
  <section class="page" style="left:360px;top:439px">
    <svg class="header-swoosh" viewBox="0 0 227 40"><path d="M67 0 C80 22 92 32 120 33 L227 29 V34 L120 37 C90 37 78 28 63 0 Z" fill="var(--sun)"/><path d="M67 0 C80 20 92 30 120 30 L227 27 V0 Z" fill="var(--navy)"/></svg>
    <div class="brand"><span class="brand-dot"></span><span>HARBOURLINE<br>PLUMBING</span></div>
    <h2 class="section-title" style="top:61px">PHOTOS &amp; VISUAL EVIDENCE</h2>
    <div class="photo-card" style="left:15px;top:81px;width:93px;height:97px">
      <h4>BEFORE</h4>
      <div class="photo-fill" role="img" aria-label="Before photo: fouled tank interior" style="background:linear-gradient(135deg,#b79a4a,#6b5a2c 60%,#e5dcc4)"></div>
      <div class="write-line" style="top:80px"></div><div class="write-line" style="top:88px"></div>
    </div>
    <div class="photo-card" style="left:119px;top:81px;width:93px;height:97px">
      <h4>DURING</h4>
      <div class="photo-fill" role="img" aria-label="During photo: tank being cleaned and serviced" style="background:linear-gradient(135deg,#d9d4c6,#5d6460 55%,#e9e4d6)"></div>
      <div class="write-line" style="top:80px"></div><div class="write-line" style="top:88px"></div>
    </div>
    <div class="photo-card" style="left:68px;top:187px;width:93px;height:97px">
      <h4>AFTER</h4>
      <div class="photo-fill" role="img" aria-label="After photo: new pipe fittings under a basin" style="background:linear-gradient(135deg,#8c96a0,#d8dadc 55%,#f1f1ef)"></div>
      <div class="write-line" style="top:80px"></div><div class="write-line" style="top:88px"></div>
    </div>
    <div class="footer-band"></div>
    <div class="footer-url">harbourlineplumbing.com.au</div>
    <div class="footer-page">Page 5</div>
  </section>

  <!-- Page 6 -->
  <section class="page" style="left:613px;top:439px">
    <svg class="header-swoosh" viewBox="0 0 227 40"><path d="M67 0 C80 22 92 32 120 33 L227 29 V34 L120 37 C90 37 78 28 63 0 Z" fill="var(--sun)"/><path d="M67 0 C80 20 92 30 120 30 L227 27 V0 Z" fill="var(--navy)"/></svg>
    <div class="brand"><span class="brand-dot"></span><span>HARBOURLINE<br>PLUMBING</span></div>
    <h2 class="section-title" style="top:81px">RECOMMENDATIONS</h2>
    <div class="priority" style="left:38px;top:101px"><span class="badge" style="background:var(--red)"></span><div><strong>Urgent</strong><small>Immediate attention required to prevent damage, risk, or failure</small></div></div>
    <div class="priority" style="left:38px;top:132px"><span class="badge" style="background:var(--amber)"></span><div><strong>Non-Urgent</strong><small>Recommended repairs or improvements</small></div></div>
    <div class="priority" style="left:38px;top:164px"><span class="badge" style="background:var(--green)"></span><div><strong>Preventative Maintenance</strong><small>Advisory actions to reduce future issues</small></div></div>
    <h2 class="section-title" style="top:199px">LIMITATIONS &amp; EXCLUSIONS</h2>
    <div class="bullet" style="left:39px;top:221px"><span class="drop"></span>Areas not inspected due to access restrictions</div>
    <div class="bullet" style="left:39px;top:232px"><span class="drop"></span>Components concealed or not visible at time of inspection</div>
    <div class="bullet" style="left:39px;top:243px"><span class="drop"></span>Assumptions made based on visible conditions</div>
    <div class="bullet" style="left:39px;top:254px"><span class="drop"></span>Items outside the agreed scope of works</div>
    <div class="footer-band"></div>
    <div class="footer-url">harbourlineplumbing.com.au</div>
    <div class="footer-page">Page 6</div>
  </section>

  <!-- Page 7 -->
  <section class="page" style="left:866px;top:439px">
    <svg class="header-swoosh" viewBox="0 0 227 40"><path d="M67 0 C80 22 92 32 120 33 L227 29 V34 L120 37 C90 37 78 28 63 0 Z" fill="var(--sun)"/><path d="M67 0 C80 20 92 30 120 30 L227 27 V0 Z" fill="var(--navy)"/></svg>
    <div class="brand"><span class="brand-dot"></span><span>HARBOURLINE<br>PLUMBING</span></div>
    <h2 class="section-title" style="top:73px;left:10px">CONCLUSION</h2>
    <div class="bullet" style="left:44px;top:91px"><span class="drop"></span>Summary of findings and works completed</div>
    <div class="bullet" style="left:44px;top:102px"><span class="drop"></span>Confirmation of current system status</div>
    <div class="bullet" style="left:44px;top:113px"><span class="drop"></span>Any recommended next steps or follow-up actions</div>
    <p class="label-bold" style="left:34px;top:130px">Summary Notes:</p>
    <div class="write-line" style="left:34px;top:148px;width:160px"></div>
    <div class="write-line" style="left:34px;top:164px;width:160px"></div>
    <div class="write-line" style="left:34px;top:179px;width:160px"></div>
    <h2 class="section-title" style="top:199px;left:10px">SIGN-OFF</h2>
    <div class="field" style="left:40px;top:220px;width:154px">Technician / Contractor Name:<span class="rule"></span></div>
    <div class="field" style="left:40px;top:231px;width:154px">Company Name:<span class="rule"></span></div>
    <div class="field" style="left:40px;top:241px;width:154px">Signature:<span class="rule"></span></div>
    <div class="field" style="left:40px;top:252px;width:154px">Date:<span class="rule"></span></div>
    <div class="footer-band"></div>
    <div class="footer-url">harbourlineplumbing.com.au</div>
    <div class="footer-page">Page 7</div>
  </section>

</main>
</body>
</html>
```